Affiliate Flyer

We are looking for a new affiliate flyer. Currently the flyer is based on a black background and we want it to be a cleaner look. We have updated our logo and I include a copy.
I also enclose our current flyer so you can see the content.
This new design needs to be either in a high res PSD, IDML file with full graphics. It is A5.
Some of the wording needs updating so i will list what needs changing:-
Get 5% off fees page:
- selling property for over 8 years, should be 11 years
- saved £20 million pounds, should be £41 million
Smart way to sell your house page:
- 7,000 homes sold, should be 8,500 homes sold
- £20m saved, should be £41m

```html
<!DOCTYPE html>
<html lang="en">
<head>
<meta charset="utf-8">
<title>Affiliate Flyer – 5% Off Fees</title>
<link rel="stylesheet" href="https://fonts.googleapis.com/css2?family=Open+Sans:wght@400;600;700;800&display=swap">
<style>
  :root {
    --green: #8cc63f;
    --orange: #f39424;
    --text: #4a4a4a;
    --ink: #3d3d3d;
    --paper: #ffffff;
    --badge-a: #dff0f2;
    --badge-b: #ece4f0;
    --badge-c: #e2ecf6;
    --logo-mark: #8cc63f;
  }
  * { margin: 0; padding: 0; box-sizing: border-box; }
  html, body {
    width: 807px;
    height: 1200px;
    overflow: hidden;
    background: var(--paper);
  }
  .flyer {
    position: relative;
    width: 807px;
    height: 1200px;
    background: var(--paper);
    font-family: "Open Sans", Arial, sans-serif;
    color: var(--text);
  }
  .headline {
    position: absolute;
    top: 28px;
    right: 52px;
    text-align: right;
    color: var(--green);
    font-weight: 700;
    font-size: 132px;
    line-height: 120px;
    letter-spacing: -3px;
  }
  .code-box {
    position: absolute;
    left: 332px;
    top: 440px;
    width: 423px;
    height: 125px;
    border: 2px solid var(--green);
  }
  .copy {
    position: absolute;
    left: 36px;
    width: 740px;
    font-size: 23.5px;
    line-height: 34px;
    color: var(--text);
  }
  .copy--intro { top: 586px; }
  .copy--history { top: 734px; }
  .highlight { color: var(--orange); }
  .partners {
    position: absolute;
    top: 928px;
    left: 36px;
    display: flex;
    gap: 30px;
  }
  .partner-badge {
    height: 72px;
    border-radius: 8px;
  }
  .partner-badge--one { width: 222px; background: var(--badge-a); }
  .partner-badge--two { width: 152px; background: var(--badge-b); }
  .partner-badge--three { width: 302px; background: var(--badge-c); }
  .call {
    position: absolute;
    left: 36px;
    top: 1046px;
  }
  .call__label {
    font-size: 25px;
    font-weight: 600;
    color: var(--ink);
    line-height: 32px;
  }
  .call__number {
    font-size: 47px;
    font-weight: 700;
    color: var(--green);
    line-height: 60px;
    letter-spacing: 0.5px;
  }
  .brand {
    position: absolute;
    left: 410px;
    top: 1060px;
    display: flex;
    align-items: center;
    gap: 18px;
  }
  .brand__mark {
    width: 74px;
    height: 74px;
    background: var(--logo-mark);
  }
  .brand__name {
    font-size: 40px;
    font-weight: 700;
    color: var(--ink);
    line-height: 1;
  }
</style>
</head>
<body>
  <main class="flyer">
    <h1 class="headline">Get 5% off<br>fees by<br>quoting:</h1>

    <div class="code-box" aria-label="Affiliate code space"></div>

    <p class="copy copy--intro">If you're looking for a modern, established, low-cost and proven method of estate agency then look no further - <span class="highlight">for a fee of £495 + vat we can sell your home</span>.</p>

    <p class="copy copy--history">We've been selling property for over 11 years, successfully completing on thousands of sales nationwide and delivering a service that's modernised estate agency, and saved over <span class="highlight">£41 million pounds in traditional agency fees.</span></p>

    <div class="partners" aria-label="Property listing partners">
      <div class="partner-badge partner-badge--one"></div>
      <div class="partner-badge partner-badge--two"></div>
      <div class="partner-badge partner-badge--three"></div>
    </div>

    <div class="call">
      <p class="call__label">Call today:</p>
      <p class="call__number">0800 555 0199</p>
    </div>

    <div class="brand">
      <span class="brand__mark"></span>
      <span class="brand__name">Homestead Hub</span>
    </div>
  </main>
</body>
</html>
```